Bref créative
Marketing Brochure for a Real Cat Spa
Velvet Whisker Grooming Spa & Boutique
Tranquility.....it's a cat thing
I have a logo, and text attached for the brochure. I'm looking for a spa feel to the brochure. If you can use the logo colors as well as some tans, browns and blacks thrown in to match our actual spa, that would be great. Please refrain from using the light green part of the logo. I'm not crazy about the lighter green. I prefer richer colors.
Animals
Personal, Caring, Eco-conscious, and modern and cutting edge. We are the first cat spa in the world, so I really want this to be a special brochure if possible.
I have a welcome section to put on one side of the brochure and a spa menu to add to the other side of the brochure.
This is the welcome section that would go first before the spa menu
This is a brief list of our spa menu.
Our Logo with our company name is attached. Also, it would be great to arrange our contact info (address, email, etc) on the back page of the brochure, at the bottom.
Our logo without our company name.
This is our logo with the text.
These are some brochure designs that I liked or found interesting.
Cat Logo with no text
Cute cat pic to use on brocuhre.

```html
<!DOCTYPE html>
<html lang="en">
<head>
<meta charset="utf-8">
<title>Velvet Whisker Grooming Spa &amp; Boutique – Brochure</title>
<link href="https://fonts.googleapis.com/css2?family=Great+Vibes&family=Lato:ital,wght@0,300;0,400;0,700;1,400&display=swap" rel="stylesheet">
<style>
  :root{
    --page:#e4e0da;
    --ink:#1b1816;
    --cream:#f7f4ef;
    --white:#ffffff;
    --tan:#b7a78e;
    --taupe:#8a7d6b;
    --mocha:#5b4f43;
    --espresso:#2a2420;
    --olive:#5d6b27;
    --stone-hi:#c9d1dc;
    --stone-lo:#6f7c8e;
  }
  *{box-sizing:border-box;margin:0;padding:0}
  html,body{width:1200px;height:926px;overflow:hidden}
  body{background:var(--page);font-family:"Lato",sans-serif;color:var(--ink);position:relative}
  .spread{position:absolute;left:30px;width:1140px;height:430px;display:flex;box-shadow:0 4px 14px rgba(0,0,0,.25);overflow:hidden}
  .spread--outside{top:20px}
  .spread--inside{top:476px;background:var(--white)}
  .panel{width:380px;height:100%;position:relative;overflow:hidden}
  .photo{position:absolute}
  /* outside flap */
  .flap{background:linear-gradient(160deg,var(--taupe),var(--mocha))}
  .flap .photo{left:0;top:0;width:100%;height:112px;background:linear-gradient(120deg,#d8cfc2,#7d6f5f 60%,#3f362e)}
  .flap .curve{position:absolute;left:0;top:100px;width:100%;height:60px}
  .flap .copy{position:absolute;left:26px;right:26px;top:150px;color:var(--cream);font-size:9.5px;line-height:1.55;font-weight:300}
  .flap .copy p{margin-bottom:8px}
  .dropcap{float:left;font-family:"Great Vibes",cursive;font-size:46px;line-height:.8;margin:2px 6px 0 0;color:var(--white)}
  .flap .band{position:absolute;left:0;bottom:0;width:100%;height:22px;background:var(--espresso)}
  /* back panel */
  .back{background:linear-gradient(180deg,#cfc6b8,var(--tan))}
  .back .photo{left:0;top:0;width:100%;height:92px;background:linear-gradient(90deg,#3b342e,#8d8276 50%,#3b342e)}
  .back .lead{position:absolute;top:104px;left:30px;right:30px;text-align:center;font-size:9.5px;line-height:1.6;color:var(--espresso)}
  .back .lead strong{display:block;font-size:11px;margin:6px 0 2px;color:var(--olive)}
  .back .contact{position:absolute;left:0;bottom:0;width:100%;height:92px;background:var(--ink);color:var(--cream);text-align:center;font-size:9.5px;line-height:1.6;padding-top:18px}
  /* cover */
  .cover{background:var(--white)}
  .cover .brand{position:absolute;top:34px;left:0;width:100%;text-align:center}
  .brand .mark{display:block;width:54px;height:54px;border-radius:50%;background:var(--olive);margin:0 auto 8px}
  .brand .name{font-family:"Great Vibes",cursive;font-size:42px;color:var(--ink);line-height:1}
  .brand .sub{font-family:"Great Vibes",cursive;font-size:24px;color:var(--ink);line-height:1.1}
  .cover .tagline{position:absolute;top:188px;width:100%;text-align:center;font-family:"Great Vibes",cursive;font-size:19px;color:var(--olive)}
  .cover .rule{position:absolute;top:218px;left:0;width:100%;height:16px;background:var(--ink)}
  .cover .photo{left:0;top:234px;width:100%;height:196px;background:radial-gradient(ellipse at 50% 40%,var(--stone-hi),var(--stone-lo) 70%,#3e4756)}
  /* inside */
  .menu{width:760px;position:relative}
  .menu .head{height:66px;text-align:center;padding-top:8px}
  .menu .head h1{font-family:"Great Vibes",cursive;font-weight:400;font-size:34px;line-height:1}
  .menu .head p{font-family:"Great Vibes",cursive;font-size:16px;color:var(--mocha)}
  .menu .cols{display:flex;gap:30px;padding:4px 30px 0;height:176px}
  .menu .col{flex:1;font-size:9px;line-height:1.5;color:var(--espresso)}
  .menu h2{font-size:10.5px;font-weight:700;color:var(--olive);margin:6px 0 2px}
  .menu ul{list-style:none}
  .menu .photo{left:0;bottom:0;width:760px;height:188px;background:linear-gradient(100deg,#f1ece4,#cbbfae 45%,#8e7f6c)}
  .badge{position:absolute;width:88px;height:88px;border-radius:50%;background:var(--mocha);color:var(--cream);font-size:8.5px;line-height:1.35;text-align:center;display:flex;align-items:center;justify-content:center;padding:10px}
  .badge--one{left:470px;bottom:92px}
  .badge--two{left:570px;bottom:36px;background:var(--espresso)}
  .welcome{background:var(--espresso);color:var(--cream)}
  .welcome .photo-top{left:190px;top:0;width:190px;height:130px;background:linear-gradient(135deg,#d9d3ca,#6c655d)}
  .welcome .photo-bottom{left:190px;bottom:0;width:190px;height:120px;background:linear-gradient(135deg,#8b8379,#2f2a26)}
  .welcome .copy{position:absolute;left:22px;top:140px;width:330px;font-size:9.5px;line-height:1.6;font-weight:300}
  .welcome .copy p{margin-bottom:8px}
</style>
</head>
<body>

<section class="spread spread--outside" aria-label="Brochure outside">
  <div class="panel flap">
    <div class="photo" role="img" aria-label="Photo of a cat relaxing on a soft spa towel"></div>
    <svg class="curve" viewBox="0 0 380 60" preserveAspectRatio="none" aria-hidden="true"><path d="M0 30 C120 0 260 60 380 10 L380 0 L0 0 Z" fill="#f7f4ef" opacity=".9"/></svg>
    <div class="copy">
      <p><span class="dropcap">W</span>hen you bring your cat to us, you are giving them a calm and gentle retreat made just for felines. Every visit is quiet, unhurried and tailored to your companion.</p>
      <p>Our groomers are trained in feline handling and use eco-conscious products that are kind to coats, skin and the planet.</p>
      <p>From a soothing bath to a full pampering day, each service is designed to leave your cat relaxed, clean and content.</p>
    </div>
    <div class="band"></div>
  </div>

  <div class="panel back">
    <div class="photo" role="img" aria-label="Photo of smooth spa stones and candles"></div>
    <div class="lead">
      <p>A serene space where every cat is treated with patience, care and respect.</p>
      <strong>Hours of Care</strong>
      <p>Tuesday to Saturday, 9 am – 6 pm<br>Appointments recommended</p>
      <strong>Gift Certificates</strong>
      <p>Share tranquility with a friend and their favourite feline.</p>
    </div>
    <div class="contact">
      214 Willow Lane, Fairhaven<br>
      (555) 013-2740<br>
      hello@velvetwhiskerspa.com
    </div>
  </div>

  <div class="panel cover">
    <div class="brand">
      <span class="mark" aria-hidden="true"></span>
      <div class="name">Velvet Whisker</div>
      <div class="sub">Grooming Spa &amp; Boutique</div>
    </div>
    <div class="tagline">Tranquility.....it's a cat thing</div>
    <div class="rule"></div>
    <div class="photo" role="img" aria-label="Photo of stacked blue-grey spa stones"></div>
  </div>
</section>

<section class="spread spread--inside" aria-label="Brochure inside">
  <div class="menu">
    <header class="head">
      <h1>Velvet Whisker Grooming Spa &amp; Boutique</h1>
      <p>A Menu of Feline Spa Treatments</p>
    </header>
    <div class="cols">
      <div class="col">
        <h2>Signature Bath</h2>
        <p>Gentle wash, conditioning rinse, warm towel dry and a soft brush out.</p>
        <h2>Deluxe Bath</h2>
        <p>Signature bath with coat treatment, nail trim and ear cleaning.</p>
      </div>
      <div class="col">
        <h2>Other Services</h2>
        <ul>
          <li>Nail Trim</li>
          <li>Ear Cleaning</li>
          <li>De-shedding Treatment</li>
          <li>Lion Cut</li>
        </ul>
        <h2>Boutique</h2>
        <p>Natural treats, toys and grooming goods.</p>
      </div>
    </div>
    <div class="photo" role="img" aria-label="Photo of a white kitten lying on its back"></div>
    <div class="badge badge--one">All of our products are natural and eco-friendly</div>
    <div class="badge badge--two">Every visit ends with a calm cuddle</div>
  </div>

  <div class="panel welcome">
    <div class="photo photo-top" role="img" aria-label="Photo of a cat being gently groomed"></div>
    <div class="copy">
      <p><span class="dropcap">V</span>elvet Whisker Grooming Spa &amp; Boutique is the first spa in the world devoted only to cats.</p>
      <p>Our calm spa rooms, soft lighting and quiet music create a peaceful setting where your cat can unwind while being cared for by people who love them.</p>
      <p>Welcome to our family.</p>
    </div>
    <div class="photo photo-bottom" role="img" aria-label="Photo of a resting tabby cat"></div>
  </div>
</section>

</body>
</html>
```